Standard Company Posters / Notices

We have manufacturing sites, across the sites there are notices that managers put up, sometimes like a poster or door notice. These are not in any standard format or follow any standard layout. We wanted to create a notice template that could be adopted with layout guidance for all our internal notices. Some examples of the notices are below. We have three different sites so we would want to interchange the logo to suit the location, I have also added some images used for our values awards as examples of the look we like.

Target Market(s)

Employees

Industry/Entity Type

Food Manufacturing

Requirements
Must have
• Flexible for the site teams to amend to suit their needs.

```html
<!DOCTYPE html>
<html lang="en">
<head>
<meta charset="utf-8">
<title>Site Notices</title>
<link href="https://fonts.googleapis.com/css2?family=Bebas+Neue&family=Arimo:wght@400;700&display=swap" rel="stylesheet">
<style>
  :root {
    --page: #ffffff;
    --panel: #bbbcbe;
    --sheet: #f3f3f3;
    --ink: #111111;
    --red: #e31e24;
    --green: #3aa935;
    --rule: #333333;
  }
  * { box-sizing: border-box; margin: 0; padding: 0; }
  html, body { width: 1092px; height: 1200px; overflow: hidden; background: var(--page); }
  .board { position: relative; width: 1092px; height: 1200px; }
  .panel { position: absolute; background: var(--panel); }
  .sheet { position: absolute; background: var(--sheet); box-shadow: 0 2px 4px rgba(0,0,0,.18); color: var(--ink); }
  .display { font-family: "Bebas Neue", "Arial Narrow", sans-serif; font-weight: 400; }
  .body-text { font-family: "Arimo", Arial, sans-serif; }
  .accent { color: var(--red); }
  .brand { position: absolute; font-family: "Arimo", Arial, sans-serif; font-weight: 700; color: var(--green); white-space: nowrap; }

  /* Phones notice */
  .notice-phones .symbol { position: absolute; left: 70px; top: 47px; width: 270px; height: 270px; }
  .notice-phones .message { position: absolute; left: 0; top: 350px; width: 100%; text-align: center; font-size: 30px; line-height: 34px; }
  .notice-phones .brand { left: 0; width: 100%; text-align: center; top: 505px; font-size: 17px; }

  /* Room checklist */
  .notice-room .title { position: absolute; left: 23px; top: 20px; font-size: 50px; line-height: 40px; }
  .notice-room .checklist { position: absolute; left: 175px; top: 23px; width: 136px; list-style: none; }
  .notice-room .checklist li { height: 25px; margin-bottom: 7.8px; border: 1px solid var(--rule); font-family: "Arimo", Arial, sans-serif; font-size: 14px; line-height: 23px; padding-left: 11px; }
  .notice-room .brand { left: 23px; top: 392px; font-size: 15px; color: var(--ink); display: flex; align-items: center; gap: 6px; }
  .notice-room .brand .mark { width: 14px; height: 14px; background: var(--red); }

  /* Changing room notice */
  .notice-changing { text-align: center; }
  .notice-changing .headline { position: absolute; left: 0; width: 100%; top: 70px; font-size: 64px; line-height: 70px; }
  .notice-changing .subhead { position: absolute; left: 0; width: 100%; top: 139px; font-size: 43px; line-height: 46px; }
  .notice-changing .divider { position: absolute; left: 41px; width: 379px; top: 204px; border-top: 1px solid var(--rule); }
  .notice-changing .note { position: absolute; left: 0; width: 100%; top: 225px; font-size: 21px; line-height: 24px; }

  /* Composite panel warning */
  .notice-panel .symbol { position: absolute; left: 91px; top: 44px; width: 152px; height: 132px; }
  .notice-panel .message { position: absolute; left: 30px; width: 274px; top: 211px; text-align: center; font-size: 13.6px; line-height: 19px; }
  .notice-panel .message strong { color: var(--red); font-weight: 700; font-size: 14.5px; letter-spacing: .3px; }
  .notice-panel .penalty { position: absolute; left: 29px; top: 322px; width: 275px; height: 38px; border: 2px solid var(--ink); border-radius: 7px; text-align: center; font-size: 13.6px; line-height: 16px; padding-top: 2px; }
  .notice-panel .penalty strong { color: var(--red); }
  .notice-panel .designer { position: absolute; left: 30px; top: 411px; }
  .notice-panel .designer .role { display: block; font-size: 6.5px; color: var(--red); letter-spacing: .4px; text-transform: uppercase; }
  .notice-panel .designer .name { display: block; font-size: 11.5px; font-weight: 700; margin-top: 2px; }
  .notice-panel .brand { right: 30px; top: 416px; font-size: 14px; }
</style>
</head>
<body>
<main class="board">
  <div class="panel" style="left:40px;top:40px;width:531px;height:644px"></div>
  <div class="panel" style="left:614px;top:40px;width:442px;height:535px"></div>
  <div class="panel" style="left:40px;top:723px;width:531px;height:437px"></div>
  <div class="panel" style="left:614px;top:623px;width:442px;height:537px"></div>

  <section class="sheet notice-phones" style="left:104px;top:82px;width:402px;height:561px">
    <svg class="symbol" viewBox="0 0 270 270" aria-hidden="true">
      <rect x="90" y="64" width="92" height="146" rx="12" fill="#111"/>
      <rect x="101" y="80" width="70" height="96" fill="#f3f3f3"/>
      <circle cx="136" cy="193" r="9" fill="#f3f3f3"/>
      <circle cx="135" cy="135" r="124" fill="none" stroke="#e31e24" stroke-width="21"/>
      <line x1="47" y1="223" x2="223" y2="47" stroke="#e31e24" stroke-width="21"/>
    </svg>
    <p class="message display">Mobile phones are <span class="accent">prohibited</span><br><span class="accent">in this area</span> unless you<br>are authorised and on the<br>concession list!</p>
    <p class="brand">BRENIN FOODS PACKING</p>
  </section>

  <section class="sheet notice-room" style="left:667px;top:75px;width:334px;height:466px">
    <h2 class="title display">Block<br>Former<br>Room</h2>
    <ul class="checklist">
      <li>1 X Dust Pan</li><li>1 X Squeeze</li><li>1 X Brush</li><li>1 X Mop</li><li>1 X Duster</li>
      <li></li><li></li><li></li><li></li><li></li><li></li><li></li><li></li>
    </ul>
    <p class="brand"><span class="mark"></span>BRENIN DAIRY</p>
  </section>

  <section class="sheet notice-changing display" style="left:75px;top:777px;width:462px;height:331px">
    <h2 class="headline">Females/Visitors</h2>
    <p class="subhead">Changing Room Only</p>
    <div class="divider"></div>
    <p class="note">No Male Dairy Operatives</p>
  </section>

  <section class="sheet notice-panel body-text" style="left:667px;top:659px;width:334px;height:466px">
    <svg class="symbol" viewBox="0 0 152 132" aria-hidden="true">
      <path d="M76 10 L142 118 Q145 124 138 124 L14 124 Q7 124 10 118 Z" fill="none" stroke="#e31e24" stroke-width="10" stroke-linejoin="round"/>
      <rect x="71" y="40" width="10" height="46" rx="5" fill="#111"/>
      <circle cx="76" cy="101" r="7.5" fill="#111"/>
    </svg>
    <p class="message">This wall comprises of a <strong>COMPOSITE PANEL</strong> and may contain flammable core material. It must not be penetrated to expose the insulation core without a valid permit to work document.</p>
    <p class="penalty">Failure to observe this precaution is considered a <strong>RED CARD</strong> offence.</p>
    <p class="designer"><span class="role">Principal Designer</span><span class="name">DANIEL HARTLEY</span></p>
    <p class="brand">BRENIN FOODS PACKING</p>
  </section>
</main>
</body>
</html>
```